Bauzaun- und Gerüst-Banner für Sachverständigenbüro (Arbeitssicherheit & Brandschutz)
Zielgruppe
Dienstleistungen in den Bereichen Arbeitssicherheit und Brandschutz
Zielgruppe sind vorallem Bauunternehmen, aber auch andere Unternehmen sämtlicher Branchen, sowie Kommunen und Verbände, wie Velmora, BKT, etc.
Aufgabenstellung
Es sollen ein Bauzaun-Banner und ein Gerüst-Banner designed werden, dabei wäre mir wichtig, dass den Betrachter klar wird, dass wir nicht nur Baustellen-Koordination können. Wir sind seit 15 Jahren am Markt und oft meinen unsere Kunden/Auftraggeber, dass wir nur Arbeitssicherheit auf Baustellen machen. Das ist so nicht richtig, es ist zwar unser Hauptgewerk, aber können und machen noch ganz viele andere Dienstleistungen in den Bereichen Arbeitssicherheit und Brandschutz, wie da wären:
- Sicherheits- und Gesundheitsschutz-Koordination (SiGeKo)
- Probenahme, Ausschreibung und Koordination von Schadstoffsanierungen
- externe Fachkräfte für Arbeitssicherheit (Sifa)
- externe Brandschutzbeauftragte
- Brandschutzerziehung und -aufklärung
- Prüfservice für Anlagen und Betriebsmittel
Zudem haben wir 2023 noch eine Akademie gegründet (trelwin Akademie UG), in wir viele Seminare in den Bereichen Arbeitssicherheit und Brandschutz anbieten, wie:
- Fachkraft für Arbeitssicherheit (Sifa 3.0)
- Sicherheitsbeauftragte
- Brandschutzbeauftragte
- Brandschutzhelfer
- Feuerlöschtraining
- Evakuierungstraining
- Havarie-/Leckagetraining
- Train-the-Trainer Diisocyanate
- Anwenderschulung Diisocyanate
- Arbeitssicherheit für Azubis und ausbildende Betriebe

```html
<!DOCTYPE html>
<html lang="de">
<head>
<meta charset="utf-8">
<title>Bauzaun-Banner – trelwin.de</title>
<link rel="stylesheet" href="https://fonts.googleapis.com/css2?family=Outfit:wght@300;400;700&family=Kalam:wght@400&display=swap">
<style>
  :root {
    --page-bg: #f2f2f2;
    --brand-blue-deep: #2a3a88;
    --brand-blue-light: #4657a0;
    --brand-red: #ee3540;
    --white: #ffffff;
  }
  html, body {
    margin: 0;
    padding: 0;
    width: 1200px;
    height: 900px;
    overflow: hidden;
    background: var(--page-bg);
  }
  .banner {
    position: absolute;
    left: 20px;
    top: 158px;
    width: 1160px;
    height: 585px;
    display: flex;
    box-shadow: 0 6px 18px rgba(0,0,0,0.12);
  }
  .banner__message {
    position: relative;
    width: 903px;
    height: 100%;
    background: linear-gradient(120deg, var(--brand-blue-deep) 0%, var(--brand-blue-light) 60%, var(--brand-blue-light) 100%);
    color: var(--white);
    font-family: "Outfit", sans-serif;
  }
  .headline {
    position: absolute;
    left: 58px;
    top: 48px;
    margin: 0;
    font-weight: 700;
    font-size: 150px;
    line-height: 127px;
    letter-spacing: -1px;
  }
  .subline {
    position: absolute;
    left: 58px;
    top: 453px;
    margin: 0;
    font-weight: 300;
    font-size: 27px;
    line-height: 36px;
    letter-spacing: -0.3px;
  }
  .banner__brand {
    position: relative;
    flex: 1;
    background: var(--brand-red);
    color: var(--white);
    font-family: "Outfit", sans-serif;
  }
  .brand-mark {
    position: absolute;
    left: 24px;
    display: flex;
    align-items: center;
    gap: 10px;
  }
  .brand-mark__dot {
    width: 30px;
    height: 30px;
    border-radius: 50%;
    background: var(--white);
    flex: none;
  }
  .brand-mark__text {
    font-weight: 400;
    font-size: 27px;
    line-height: 1;
  }
  .brand-mark--office { top: 102px; }
  .brand-mark--academy { top: 283px; }
  .brand-note {
    position: absolute;
    left: 64px;
    font-size: 8px;
    font-weight: 400;
  }
  .brand-note--top { top: 92px; }
  .brand-note--bottom { top: 134px; }
  .academy-label {
    position: absolute;
    left: 64px;
    top: 311px;
    font-weight: 400;
    font-size: 20px;
    letter-spacing: 1px;
  }
  .academy-claim {
    position: absolute;
    left: 0;
    right: 0;
    top: 342px;
    text-align: center;
    font-family: "Kalam", cursive;
    font-size: 14px;
  }
  .web-address {
    position: absolute;
    left: 0;
    right: 0;
    top: 494px;
    text-align: center;
    font-weight: 700;
    font-size: 23px;
  }
</style>
</head>
<body>
  <section class="banner">
    <div class="banner__message">
      <h1 class="headline">Wir sichern<br>mehr als nur<br>Gerüste.</h1>
      <p class="subline">Bei uns bekommst du Arbeitssicherheit PLUS – von SiGeKo bis<br>Feuerlöschtraining. Seit 15 Jahren alles im Griff!</p>
    </div>
    <aside class="banner__brand">
      <span class="brand-note brand-note--top">Sachverständigenbüro</span>
      <div class="brand-mark brand-mark--office">
        <span class="brand-mark__dot"></span>
        <span class="brand-mark__text">trelwin.de</span>
      </div>
      <span class="brand-note brand-note--bottom">Arbeitssicherheit &amp; Brandschutz</span>

      <div class="brand-mark brand-mark--academy">
        <span class="brand-mark__dot"></span>
        <span class="brand-mark__text">trelwin.de</span>
      </div>
      <span class="academy-label">Akademie</span>
      <p class="academy-claim">Hier entstehen Sicherheitsexperten!</p>

      <p class="web-address">www.trelwin.de</p>
    </aside>
  </section>
</body>
</html>
```